Bref créative
business card for vegan prepared foods company
ZELO, taste the bright side
Simple
Petra Valdoni
Chef/Owner
www.zelofoods.example
zelofoods@mailbox.example
I would my business card to have on one side logo+web address, on the other side logo+ the rest of the info
logo and website address

```html
<!DOCTYPE html>
<html lang="en">
<head>
<meta charset="utf-8">
<title>Zelo stationery set</title>
<link href="https://fonts.googleapis.com/css2?family=Nunito:wght@400;700&display=swap" rel="stylesheet">
<style>
  :root {
    --bg: #2a2a2a;
    --green: #2e9a46;
    --green-dark: #4b7a3a;
    --green-faint: #3aa852;
    --brown: #5b3b2b;
    --paper: #ffffff;
    --ink: #6b6b6b;
    --line: #cfcfcf;
  }
  * { box-sizing: border-box; margin: 0; padding: 0; }
  html, body { width: 1200px; height: 773px; overflow: hidden; background: var(--bg); }
  body { position: relative; font-family: "Nunito", sans-serif; color: var(--ink); }
  .piece { position: absolute; background: var(--paper); overflow: hidden; }

  .brand { display: flex; align-items: center; gap: 6px; color: var(--brown); font-weight: 700; letter-spacing: 1px; }
  .brand-dot { border-radius: 50%; background: var(--green); flex: none; }
  .tagline { color: var(--green); font-size: 7px; }

  /* folder */
  .folder-cover { left: 40px; top: 60px; width: 260px; height: 360px; }
  .folder-cover .brand { position: absolute; left: 50px; top: 120px; font-size: 38px; }
  .folder-cover .brand-dot { width: 22px; height: 22px; }
  .folder-cover .tagline { position: absolute; left: 54px; top: 172px; font-size: 9px; }
  .folder-cover .band { position: absolute; left: 0; bottom: 0; width: 100%; height: 110px; background: var(--green); }
  .folder-cover .band-line { position: absolute; left: 0; bottom: 110px; width: 100%; height: 4px; background: var(--green-faint); }
  .folder-pocket { left: 300px; top: 60px; width: 260px; height: 360px; background: var(--green); }
  .folder-pocket .watermark { position: absolute; left: 30px; top: 120px; font-size: 72px; font-weight: 700; color: var(--green-faint); }

  /* letter pages */
  .page { top: 40px; width: 170px; height: 240px; }
  .page .stripe { height: 8px; background: var(--green); }
  .page .brand { position: absolute; right: 12px; top: 16px; font-size: 13px; }
  .page .brand-dot { width: 8px; height: 8px; }
  .page .footer { position: absolute; left: 12px; bottom: 10px; font-size: 5px; }
  .letterhead { left: 600px; }
  .invoice { left: 790px; }
  .continuation { left: 980px; }
  .invoice h2 { position: absolute; left: 12px; top: 38px; font-size: 9px; color: var(--brown); }
  .invoice .number { position: absolute; right: 12px; top: 40px; font-size: 6px; }
  .invoice table { position: absolute; left: 12px; top: 56px; width: 146px; border-collapse: collapse; font-size: 5px; }
  .invoice th, .invoice td { border: 0.5px solid var(--line); height: 9px; text-align: left; padding-left: 2px; }
  .invoice th { background: #eef6ef; color: var(--green); }

  /* envelopes */
  .envelope-dl { left: 600px; top: 320px; width: 320px; height: 160px; }
  .envelope-dl svg { position: absolute; inset: 0; }
  .envelope-dl .brand { position: absolute; left: 128px; top: 78px; font-size: 18px; }
  .envelope-dl .brand-dot { width: 11px; height: 11px; }
  .envelope-c5 { left: 600px; top: 510px; width: 270px; height: 190px; }
  .envelope-c5 .brand { position: absolute; left: 18px; top: 18px; font-size: 18px; }
  .envelope-c5 .brand-dot { width: 11px; height: 11px; }
  .envelope-c5 .window { position: absolute; right: 18px; bottom: 22px; width: 110px; height: 40px; background: #e6e6e6; }

  /* business cards */
  .card { width: 210px; height: 120px; border-radius: 10px; }
  .card .brand { font-size: 24px; }
  .card .brand-dot { width: 14px; height: 14px; }
  .card-front { background: var(--green-dark); }
  .card-front .brand { position: absolute; left: 52px; top: 36px; color: #ffffff; }
  .card-front .web { position: absolute; left: 54px; top: 74px; font-size: 8px; color: #ffffff; }
  .card-back { background: var(--paper); }
  .card-back .brand { position: absolute; left: 16px; top: 14px; }
  .card-back .contact { position: absolute; left: 16px; top: 58px; font-size: 7.5px; line-height: 1.5; }
  .card-back .name { color: var(--brown); font-weight: 700; font-size: 9px; }
  .card-back .strip { position: absolute; right: 0; top: 0; width: 8px; height: 100%; background: var(--green); }
  .pos-a { left: 40px; top: 470px; }
  .pos-b { left: 270px; top: 470px; }
  .pos-c { left: 920px; top: 520px; }
  .pos-d { left: 920px; top: 650px; }
</style>
</head>
<body>

  <section class="piece folder-cover">
    <div class="brand"><span class="brand-dot"></span>ZELO</div>
    <p class="tagline">ZELO, taste the bright side</p>
    <div class="band-line"></div>
    <div class="band"></div>
  </section>
  <section class="piece folder-pocket">
    <div class="watermark">ZELO</div>
  </section>

  <section class="piece page letterhead">
    <div class="stripe"></div>
    <div class="brand"><span class="brand-dot"></span>ZELO</div>
    <p class="footer">www.zelofoods.example · zelofoods@mailbox.example</p>
  </section>

  <section class="piece page invoice">
    <div class="stripe"></div>
    <div class="brand"><span class="brand-dot"></span>ZELO</div>
    <h2>Invoice</h2>
    <p class="number">No. 001</p>
    <table>
      <tr><th>Item</th><th>Qty</th><th>Price</th><th>Total</th></tr>
      <tr><td></td><td></td><td></td><td></td></tr>
      <tr><td></td><td></td><td></td><td></td></tr>
      <tr><td></td><td></td><td></td><td></td></tr>
      <tr><td></td><td></td><td></td><td></td></tr>
    </table>
    <p class="footer">www.zelofoods.example · zelofoods@mailbox.example</p>
  </section>

  <section class="piece page continuation">
    <div class="stripe"></div>
    <div class="brand"><span class="brand-dot"></span>ZELO</div>
    <p class="footer">www.zelofoods.example · zelofoods@mailbox.example</p>
  </section>

  <section class="piece envelope-dl">
    <svg width="320" height="160" viewBox="0 0 320 160" aria-hidden="true">
      <polyline points="0,0 160,70 320,0" fill="none" stroke="var(--line)" stroke-width="1"/>
    </svg>
    <div class="brand"><span class="brand-dot"></span>ZELO</div>
  </section>

  <section class="piece envelope-c5">
    <div class="brand"><span class="brand-dot"></span>ZELO</div>
    <div class="window"></div>
  </section>

  <section class="piece card card-front pos-a">
    <div class="brand"><span class="brand-dot"></span>ZELO</div>
    <p class="web">www.zelofoods.example</p>
  </section>
  <section class="piece card card-back pos-b">
    <div class="brand"><span class="brand-dot"></span>ZELO</div>
    <div class="contact">
      <p class="name">Petra Valdoni</p>
      <p>Chef/Owner</p>
      <p>www.zelofoods.example</p>
      <p>zelofoods@mailbox.example</p>
    </div>
    <div class="strip"></div>
  </section>

  <section class="piece card card-back pos-c">
    <div class="brand"><span class="brand-dot"></span>ZELO</div>
    <div class="contact">
      <p class="name">Petra Valdoni</p>
      <p>Chef/Owner</p>
      <p>zelofoods@mailbox.example</p>
    </div>
    <div class="strip"></div>
  </section>
  <section class="piece card card-front pos-d" style="height:110px">
    <div class="brand"><span class="brand-dot"></span>ZELO</div>
    <p class="web">www.zelofoods.example</p>
  </section>

</body>
</html>
```